Laundromat Grand Opening.

Laundromat /Grand opening. One side English, one side Spanish. Include the Address, Name, Raffle/Prizes and Grand opening date.
Elmridge Wash Laundromat, 415 W. Harlan Ave. 2/7/2016. (555) 314-2297.

Coin

000000

• Eye catching. Laundry theme.

```html
<!DOCTYPE html>
<html lang="en">
<head>
<meta charset="utf-8">
<title>Elmridge Wash Laundromat – Grand Opening Flyers</title>
<link rel="stylesheet" href="https://fonts.googleapis.com/css2?family=Montserrat:wght@500;600;700;800&family=Roboto+Condensed:wght@400;700&display=swap">
<style>
  :root {
    --page-bg: #ffffff;
    --sky-top: #1f9be0;
    --sky-light: #bfe6f7;
    --sky-mid: #5fb3e6;
    --sky-deep: #2c6fc4;
    --brand-red: #c8202f;
    --white: #ffffff;
    --gold: #f6d21f;
    --gold-deep: #e9b810;
    --ink: #111111;
    --navy: #2b3282;
    --art-warm: #e9a98f;
    --art-tan: #c79a68;
    --art-red: #c92a2f;
  }
  * { margin: 0; padding: 0; box-sizing: border-box; }
  html, body {
    width: 1200px; height: 729px; overflow: hidden;
    background: var(--page-bg);
  }
  .stage { position: relative; width: 1200px; height: 729px; }

  .flyer {
    position: absolute; top: 104px;
    width: 355px; height: 520px; overflow: hidden;
    background:
      radial-gradient(ellipse 80% 14% at 50% 46%, rgba(255,255,255,0.55), rgba(255,255,255,0) 70%),
      linear-gradient(180deg, var(--sky-top) 0%, var(--sky-light) 44%, var(--sky-mid) 62%, var(--sky-deep) 100%);
    box-shadow: 0 2px 8px rgba(0,0,0,0.25);
    font-family: "Montserrat", sans-serif;
    text-align: center;
  }
  .flyer--english { left: 230px; }
  .flyer--spanish { left: 614px; }

  .hero-art {
    position: absolute; left: 34px; top: 24px;
    width: 287px; height: 196px;
    background: linear-gradient(180deg, var(--art-tan) 0%, var(--art-warm) 55%, var(--art-red) 100%);
    opacity: 0.85;
  }
  .hero-rule {
    position: absolute; left: 34px; top: 220px;
    width: 287px; height: 2px;
    background: rgba(60,90,120,0.55);
  }

  .business-name {
    position: absolute; left: 0; right: 0; top: 236px;
    line-height: 1.08;
  }
  .business-name__main {
    display: block; color: var(--brand-red);
    font-weight: 600; font-size: 27px; letter-spacing: 0.5px;
  }
  .business-name__type {
    display: block; color: var(--white);
    font-weight: 500; font-size: 27px; letter-spacing: 0.5px;
  }

  .headline {
    position: absolute; left: 0; right: 0; top: 312px;
    color: var(--gold); font-weight: 800; font-size: 50px;
    letter-spacing: 1px; line-height: 1;
    text-shadow: 0 1px 0 var(--gold-deep);
  }
  .headline-rule {
    position: absolute; left: 40px; top: 350px;
    width: 275px; height: 32px;
  }
  .subline {
    position: absolute; left: 0; right: 0; top: 380px;
    color: var(--gold); font-weight: 800; font-size: 36px;
    letter-spacing: 0.5px; line-height: 1;
    text-shadow: 0 1px 0 var(--gold-deep);
  }
  .subline--long { font-size: 28px; top: 384px; }

  .event-date {
    position: absolute; left: 0; right: 0; top: 428px;
    color: var(--ink); font-weight: 600; font-size: 23px;
    letter-spacing: 0.8px; line-height: 1;
  }
  .raffle-note {
    position: absolute; left: 0; right: 0; top: 457px;
    color: var(--white); font-weight: 700; font-size: 13px;
    letter-spacing: 1px; line-height: 1;
  }

  .address-band {
    position: absolute; left: 0; right: 0; bottom: 0;
    height: 38px; background: var(--navy);
    color: var(--white);
    font-family: "Roboto Condensed", sans-serif;
    font-size: 13.5px; line-height: 38px;
  }
</style>
</head>
<body>
<main class="stage">

  <article class="flyer flyer--english" lang="en">
    <div class="hero-art" role="img" aria-label="Illustration area: cartoon of a surprised customer among soap bubbles"></div>
    <div class="hero-rule"></div>
    <h1 class="business-name">
      <span class="business-name__main">ELMRIDGE WASH</span>
      <span class="business-name__type">LAUNDROMAT</span>
    </h1>
    <p class="headline">GRAND</p>
    <svg class="headline-rule" viewBox="0 0 275 32" aria-hidden="true">
      <polygon points="0,14 118,14 131,2 144,14 275,14 262,20 144,20 131,8 118,20 10,20" fill="var(--gold)"/>
    </svg>
    <p class="subline">OPENING!</p>
    <p class="event-date">FEBRUARY 7, 2016</p>
    <p class="raffle-note">RAFFLE &amp; PRIZES!</p>
    <footer class="address-band">415 W. Harlan Ave. &nbsp;•&nbsp; Elmridge, CA &nbsp;•&nbsp; (555) 314-2297</footer>
  </article>

  <article class="flyer flyer--spanish" lang="es">
    <div class="hero-art" role="img" aria-label="Illustration area: cartoon of a surprised customer among soap bubbles"></div>
    <div class="hero-rule"></div>
    <h1 class="business-name">
      <span class="business-name__main">ELMRIDGE WASH</span>
      <span class="business-name__type">LAUNDROMAT</span>
    </h1>
    <p class="headline">GRAN</p>
    <svg class="headline-rule" viewBox="0 0 275 32" aria-hidden="true">
      <polygon points="0,14 128,14 141,2 154,14 275,14 262,20 154,20 141,8 128,20 10,20" fill="var(--gold)"/>
    </svg>
    <p class="subline subline--long">INAUGURACIÓN</p>
    <p class="event-date">FEBRUARY 7, 2016</p>
    <p class="raffle-note">¡RIFA Y PREMIOS!</p>
    <footer class="address-band">415 W. Harlan Ave. &nbsp;•&nbsp; Elmridge, CA &nbsp;•&nbsp; (555) 314-2297</footer>
  </article>

</main>
</body>
</html>
```